kreative Verpackungen für junges Unternehmen
Sehr professionell in der Umsetzung. Bin mit dem Design und der Zusammenarbeit sehr zufrieden, auch wenn es bei der Nachbearbeitung leichte Missverständnisse gab. Definitiv weiter zu empfehlen!
Zielgruppe
Wir sind ein junges Unternehmen und suchen eine ansprechende Gestaltung unserer Verpackung für unser Produkt.
Unsere Zielgruppe sind Mütter mit Kinderwagen, Rad- und Rollerfahrer.
Aufgabenstellung
Es sollte eine positive Stimmung erzeugt werden (z.B. durch eine lachende junge Frau), das Produkt jedoch im Vordergrund stehen. Zusätzlich wäre es gut, wenn eine gewisse Wärmewirkung vermittelt wird. Es handelt sich um einen Handwärmer, welcher an Griffen befestigt werden kann und in einer Box verpackt werden soll mit folgenden Maßen: Breite/Tiefe/Höhe 80mm/60mm/130mm
Wir freuen uns auf eure kreativen Vorschläge!

```html
<!DOCTYPE html>
<html lang="de">
<head>
<meta charset="utf-8">
<title>Handwärmer – Verpackung Frontseite</title>
<link rel="stylesheet" href="https://fonts.googleapis.com/css2?family=Alegreya+Sans:wght@700&display=swap">
<style>
  :root {
    --page-bg: #f4f4f4;
    --tan: #b98c6b;
    --photo-light: #ece3d6;
    --photo-mid: #d9c0a2;
    --pink: #e6b9c6;
    --coral: #d87f63;
    --plum: #636082;
    --white: #ffffff;
    --product-light: #eef0f2;
    --product-shade: #d6d8dc;
  }
  html, body {
    margin: 0;
    width: 1200px;
    height: 1200px;
    overflow: hidden;
    background: var(--page-bg);
  }
  .canvas {
    position: relative;
    width: 1200px;
    height: 1200px;
  }
  .box-front {
    position: absolute;
    left: 359px;
    top: 209px;
    width: 480px;
    height: 783px;
    display: block;
  }
  .product-title {
    font-family: "Alegreya Sans", sans-serif;
    font-weight: 700;
    fill: var(--white);
    letter-spacing: 3px;
  }
  .icon-badge { fill: var(--plum); }
  .icon-line {
    fill: none;
    stroke: var(--white);
    stroke-width: 4;
    stroke-linecap: round;
    stroke-linejoin: round;
  }
  .icon-fill { fill: var(--white); }
</style>
</head>
<body>
<main class="canvas">
  <svg class="box-front" viewBox="578 337 773 1260" xmlns="http://www.w3.org/2000/svg">
    <defs>
      <clipPath id="front-clip">
        <rect x="578" y="337" width="773" height="1260"/>
      </clipPath>
      <linearGradient id="photo-tones" x1="0" y1="0" x2="0" y2="1">
        <stop offset="0" stop-color="var(--photo-light)"/>
        <stop offset="0.55" stop-color="var(--photo-mid)"/>
        <stop offset="1" stop-color="var(--tan)"/>
      </linearGradient>
      <linearGradient id="product-tones" x1="0" y1="0" x2="0" y2="1">
        <stop offset="0" stop-color="var(--product-light)"/>
        <stop offset="1" stop-color="var(--product-shade)"/>
      </linearGradient>
    </defs>

    <g clip-path="url(#front-clip)">
      <rect class="base-tan" x="578" y="337" width="773" height="1260" fill="var(--tan)"/>

      <rect class="lifestyle-photo" x="578" y="337" width="773" height="690"
            fill="url(#photo-tones)" role="img"
            aria-label="Foto: lachende junge Frau mit Strickschal und Mantel in winterlicher Stadtstraße"/>

      <g class="warmth-rings">
        <circle cx="1075" cy="1218" r="413" fill="var(--pink)"/>
        <circle cx="1075" cy="1218" r="353" fill="var(--coral)"/>
        <circle cx="1075" cy="1218" r="300" fill="var(--plum)"/>
      </g>

      <rect class="title-band" x="578" y="1297" width="500" height="175" fill="var(--plum)"/>

      <rect class="product-photo" x="795" y="1048" width="556" height="277" rx="40"
            fill="url(#product-tones)" role="img"
            aria-label="Produktfoto: weißer Handwärmer an einem Lenkergriff befestigt"/>

      <text class="product-title" x="652" y="1412" font-size="86" textLength="630" lengthAdjust="spacingAndGlyphs">HANDWÄRMER</text>

      <g class="use-icons">
        <g class="icon-pram">
          <circle class="icon-badge" cx="1206" cy="461" r="47"/>
          <path class="icon-fill" d="M1207 432 A 30 30 0 0 1 1237 462 L 1207 462 Z"/>
          <path class="icon-line" d="M1176 450 L1183 450 L1188 464 L1237 464 Q1232 478 1212 478 L1196 478 Q1189 476 1188 464"/>
          <path class="icon-line" d="M1196 478 L1222 488 M1222 478 L1196 488"/>
          <circle class="icon-line" cx="1193" cy="488" r="6"/>
          <circle class="icon-line" cx="1226" cy="488" r="6"/>
        </g>
        <g class="icon-bicycle">
          <circle class="icon-badge" cx="1206" cy="594" r="47"/>
          <circle class="icon-line" cx="1183" cy="605" r="13"/>
          <circle class="icon-line" cx="1230" cy="605" r="13"/>
          <path class="icon-line" d="M1183 605 L1196 580 L1222 580 L1230 605 M1196 580 L1208 605 L1222 580 M1190 575 L1200 575 M1218 572 L1226 570"/>
        </g>
        <g class="icon-scooter">
          <circle class="icon-badge" cx="1206" cy="726" r="47"/>
          <path class="icon-line" d="M1210 696 L1216 696 L1225 740 M1180 744 L1220 744"/>
          <circle class="icon-line" cx="1180" cy="744" r="6"/>
          <circle class="icon-line" cx="1227" cy="744" r="6"/>
        </g>
      </g>
    </g>
  </svg>
</main>
</body>
</html>
```